Bref créative
BRN Tek
B-cards, letter head and envelopes
I need single sided standard sized Business Card [3.5" x 2"]
use same font or others...other fonts are welcome
Simple
Gareth Pembly
CEO
482 Harlowe Street, Suite 1730
Marlow Bay, Oregon 97342
gpembly@brnqel.com
brnqel.com
-use this logo in the business cards, letterhead and envelopes.
-we are looking for designs with and with out a water mark using parts or the entire logo.

```html
<!DOCTYPE html>
<html lang="en">
<head>
<meta charset="utf-8">
<title>BRN Tek — Business Card</title>
<link rel="stylesheet" href="https://fonts.googleapis.com/css2?family=Montserrat:wght@400;500;600&display=swap">
<style>
  :root {
    --page-bg: #d9dde1;
    --card-light: #eef2f5;
    --panel-top: #2f4862;
    --panel-bottom: #4a6482;
    --text-light: #ffffff;
    --text-soft: #dfe7ef;
    --brand-blue: #1f5d8c;
    --brand-dot: #6db33f;
  }
  * { margin: 0; padding: 0; box-sizing: border-box; }
  html, body {
    width: 1200px;
    height: 969px;
    overflow: hidden;
    background: var(--page-bg);
    font-family: "Montserrat", sans-serif;
  }
  .business-card {
    position: absolute;
    left: 100px;
    top: 199px;
    width: 1000px;
    height: 571px;
    background: var(--card-light);
    border-radius: 10px;
    overflow: hidden;
    box-shadow: 0 18px 40px rgba(20, 35, 55, 0.25);
  }
  .card-panel {
    position: absolute;
    inset: 0;
    width: 1000px;
    height: 571px;
  }
  .brand-mark {
    position: absolute;
    left: 640px;
    top: 70px;
    display: flex;
    align-items: center;
    gap: 16px;
  }
  .brand-dot {
    width: 26px;
    height: 26px;
    border-radius: 50%;
    background: var(--brand-dot);
  }
  .brand-name {
    font-size: 62px;
    font-weight: 600;
    color: var(--brand-blue);
    letter-spacing: 1px;
    line-height: 1;
  }
  .person {
    position: absolute;
    left: 52px;
    top: 118px;
    color: var(--text-light);
  }
  .person-name {
    font-size: 38px;
    font-weight: 400;
    line-height: 1.1;
  }
  .person-title {
    font-size: 44px;
    font-weight: 600;
    line-height: 1.1;
  }
  .contact-list {
    position: absolute;
    left: 52px;
    top: 312px;
    list-style: none;
    color: var(--text-soft);
    font-size: 17px;
    line-height: 22px;
  }
  .website {
    position: absolute;
    left: 52px;
    top: 506px;
    color: var(--text-soft);
    font-size: 20px;
    letter-spacing: 0.5px;
  }
</style>
</head>
<body>
  <div class="business-card">
    <svg class="card-panel" viewBox="0 0 1000 571" aria-hidden="true">
      <defs>
        <linearGradient id="panelShade" x1="0" y1="0" x2="0.3" y2="1">
          <stop offset="0" stop-color="var(--panel-top)"/>
          <stop offset="1" stop-color="var(--panel-bottom)"/>
        </linearGradient>
      </defs>
      <path d="M0,90 L500,90 C565,90 560,215 630,215 L1000,215 L1000,571 L0,571 Z" fill="url(#panelShade)"/>
    </svg>

    <div class="brand-mark">
      <span class="brand-dot"></span>
      <span class="brand-name">BRN Tek</span>
    </div>

    <div class="person">
      <p class="person-name">Gareth Pembly</p>
      <p class="person-title">CEO</p>
    </div>

    <ul class="contact-list">
      <li>482 Harlowe Street, Suite 1730</li>
      <li>Marlow Bay, Oregon 97342</li>
      <li>800-555-0148</li>
      <li>414-555-0172</li>
      <li>415-555-0193</li>
      <li>415-555-0126</li>
      <li>gpembly@brnqel.com</li>
    </ul>

    <p class="website">www.brnqel.com</p>
  </div>
</body>
</html>
```